Stationery & Business Card Design For A Mobile Ultrasound Company
Ridgecrest Sonar Partners, Inc.
Professional
Martin L. Povich
Clinical Director
3187 Hawthorn Lane NE
Maplewood, KS 66892
ridgecrestsonarpartners@mailnest.example
www.ridgecrestsonarpartners.example

```html
<!DOCTYPE html>
<html lang="en">
<head>
<meta charset="utf-8">
<title>Ridgecrest Sonar Partners – Business Card</title>
<link href="https://fonts.googleapis.com/css2?family=Open+Sans:wght@400;600;700&display=swap" rel="stylesheet">
<style>
  :root {
    --page: #e9e6e2;
    --card: #ffffff;
    --brand-blue: #2c6ea6;
    --brand-red: #c7232c;
    --text-grey: #555a60;
    --icon-grey: #6b7075;
    --rule-grey: #d4d7db;
  }
  html, body {
    margin: 0;
    width: 1200px;
    height: 818px;
    overflow: hidden;
    background: var(--page);
    font-family: "Open Sans", Arial, sans-serif;
  }
  .card {
    position: absolute;
    left: 100px;
    top: 123px;
    width: 1000px;
    height: 572px;
    background: var(--card);
    border-radius: 30px;
    overflow: hidden;
    box-shadow: 0 10px 30px rgba(0,0,0,0.18);
  }
  .wordmark {
    position: absolute;
    left: 70px;
    top: 70px;
    margin: 0;
    font-size: 54px;
    font-weight: 600;
    color: var(--brand-blue);
    letter-spacing: 1px;
    line-height: 1;
    text-transform: uppercase;
  }
  .contact {
    position: absolute;
    left: 92px;
    font-size: 19px;
    line-height: 24px;
    color: var(--text-grey);
    display: flex;
    align-items: center;
    gap: 12px;
  }
  .contact svg { width: 18px; height: 18px; fill: var(--icon-grey); flex: none; }
  .contact-address { top: 196px; }
  .contact-phone { top: 282px; }
  .contact-mobile { top: 312px; }
  .contact-email { top: 342px; }
  .person {
    position: absolute;
    right: 70px;
    top: 222px;
    text-align: right;
  }
  .person-name {
    font-size: 26px;
    font-weight: 700;
    color: var(--brand-blue);
    margin: 0;
  }
  .person-title {
    font-size: 19px;
    color: var(--text-grey);
    margin: 2px 0 0;
  }
  .swoosh {
    position: absolute;
    left: 0;
    top: 0;
    width: 1000px;
    height: 572px;
  }
  .website {
    position: absolute;
    right: 62px;
    top: 452px;
    font-size: 19px;
    line-height: 24px;
    color: #ffffff;
  }
</style>
</head>
<body>
  <div class="card">
    <h1 class="wordmark">Ridgecrest Sonar</h1>

    <div class="contact contact-address">
      <svg viewBox="0 0 20 20"><path d="M10 2 1 10h3v8h5v-5h2v5h5v-8h3z"/></svg>
      <span>3187 Hawthorn Lane NE, Maplewood, KS 66892</span>
    </div>
    <div class="contact contact-phone">
      <svg viewBox="0 0 20 20"><path d="M5 2c1 0 2 3 2 4s-2 1-1 3 3 4 5 5 2-1 3-1 4 1 4 2-2 3-3 3C9 18 2 11 2 5c0-1 2-3 3-3z"/></svg>
      <span>555-014-2297</span>
    </div>
    <div class="contact contact-mobile">
      <svg viewBox="0 0 20 20"><path d="M6 1h8a1 1 0 0 1 1 1v16a1 1 0 0 1-1 1H6a1 1 0 0 1-1-1V2a1 1 0 0 1 1-1zm1 3v10h6V4zm3 11.5a1 1 0 1 0 0 2 1 1 0 0 0 0-2z"/></svg>
      <span>555-018-6630</span>
    </div>
    <div class="contact contact-email">
      <svg viewBox="0 0 20 20"><path d="M2 4h16v12H2zm1.5 1.5 6.5 5 6.5-5zM3.5 7v7.5h13V7L10 12z"/></svg>
      <span>ridgecrestsonarpartners@mailnest.example</span>
    </div>

    <div class="person">
      <p class="person-name">Martin L. Povich</p>
      <p class="person-title">Clinical Director</p>
    </div>

    <svg class="swoosh" viewBox="0 0 1000 572" aria-hidden="true">
      <path d="M0 428 C300 398 620 440 1000 356" fill="none" stroke="var(--rule-grey)" stroke-width="3"/>
      <path d="M0 448 C300 418 620 460 1000 378 L1000 398 C640 482 300 440 0 472 Z" fill="var(--brand-blue)"/>
      <path d="M0 472 C300 440 640 482 1000 398 L1000 572 L0 572 Z" fill="var(--brand-red)"/>
    </svg>

    <div class="website">www.ridgecrestsonarpartners.example</div>
  </div>
</body>
</html>
```